Email Design Creative Design Needed

Our website is called CampusLedger.org. One of our competitor(varsity scout.us.com) is using the following email creative.
http://qtr.brightvelmo.com/Affiliate/Assets/3532.html
http://qtr.brightvelmo.com/Affiliate/Assets/7921.html
http://qtr.brightvelmo.com/Affiliate/Assets/8061.html

We would like to use similar email creative without copying their exact creative. You can use the above as a guide but then come up with your own version of the creative.
The above are just concepts, please be creative and come up with your own version of it, without feeling that they have been copied. Feel free to move the components around. Also, feel free to change the colours and text.

Please find attached the CampusLedger.org logo.

Reason: We would like to receive more designs.

Industry/Entity Type

College

```html
<!DOCTYPE html>
<html lang="en">
<head>
<meta charset="utf-8">
<title>CampusLedger.org – Occupations and Next Steps</title>
<link rel="stylesheet" href="https://fonts.googleapis.com/css2?family=Exo+2:wght@400;500;600;700;800&display=swap">
<style>
  :root {
    --white: #ffffff;
    --olive: #cbc733;
    --olive-deep: #b3af22;
    --olive-edge: #9f9b1a;
    --olive-ink: #5f5c14;
    --lime: #c9ca2e;
    --brand-ink: #b4b51c;
    --sky: #0aa0cc;
    --sky-soft: #4fbfe2;
    --orange: #f24a0a;
    --orange-hot: #ff6a00;
    --footer-ink: #5a5a5a;
    --photo-top: #9fcf7a;
    --photo-mid: #6f9a56;
    --photo-low: #3f5f3a;
  }
  * { box-sizing: border-box; margin: 0; padding: 0; }
  html, body { width: 720px; height: 1200px; overflow: hidden; background: var(--white); }
  body { font-family: "Exo 2", Arial, sans-serif; }

  .email { position: relative; width: 720px; height: 1200px; overflow: hidden; background: var(--white); }

  .brand { display: flex; align-items: center; gap: 6px; }
  .brand-dot { width: 30px; height: 30px; border-radius: 50%; background: var(--lime); flex: none; }
  .brand-name { font-weight: 600; font-size: 26px; color: var(--brand-ink); letter-spacing: -0.2px; }

  .masthead { position: absolute; top: 0; left: 0; width: 720px; height: 58px; }
  .masthead .brand { position: absolute; right: 20px; top: 12px; }

  .hero-band {
    position: absolute; top: 58px; left: 0; width: 720px; height: 180px;
    background: linear-gradient(to bottom, var(--olive) 0%, var(--olive-deep) 92%);
    border-top: 4px solid var(--lime);
    border-bottom: 9px solid var(--olive-edge);
    text-align: center;
  }
  .hero-title { margin-top: 14px; font-size: 62px; font-weight: 800; color: var(--white); line-height: 1.1; }
  .hero-subtitle { margin-top: 8px; font-size: 43px; font-weight: 500; color: var(--olive-ink); line-height: 1.1; }

  .hero-photo {
    position: absolute; top: 238px; left: 0; width: 720px; height: 472px;
    background: linear-gradient(160deg, var(--photo-top) 0%, var(--photo-mid) 45%, var(--photo-low) 100%);
  }

  .cta {
    position: absolute; top: 648px; left: 0; width: 370px; height: 62px;
    background: linear-gradient(to right, var(--orange), var(--orange-hot));
    clip-path: polygon(0 0, 340px 0, 370px 62px, 0 62px);
    color: var(--white); padding: 6px 0 0 23px;
  }
  .cta-title { font-size: 22px; font-weight: 700; line-height: 1.15; }
  .cta-text { font-size: 17px; font-weight: 500; line-height: 1.3; }

  .occupations { position: absolute; top: 720px; left: 0; width: 720px; height: 408px; background: var(--sky); }
  .occupations-head, .occupation-row { display: grid; grid-template-columns: 218px 192px 1fr; }
  .occupations-head { padding: 20px 0 0 47px; font-size: 19px; font-weight: 600; color: var(--white); height: 50px; }
  .occupations-panel {
    position: absolute; top: 50px; left: 26px; width: 670px; height: 329px;
    background: var(--sky-soft); padding-top: 14px;
  }
  .occupation-row { padding-left: 21px; height: 65px; font-size: 17px; line-height: 21px; color: var(--white); }

  .footer-rule { position: absolute; top: 1128px; left: 0; width: 720px; height: 10px; background: var(--lime); }
  .footer { position: absolute; top: 1138px; left: 0; width: 720px; height: 62px; }
  .footer .brand { position: absolute; left: 33px; top: 16px; }
  .footer .brand-dot { width: 26px; height: 26px; }
  .footer .brand-name { font-size: 23px; }
  .footer-links { position: absolute; left: 371px; top: 20px; font-size: 18px; color: var(--footer-ink); }
</style>
</head>
<body>
<div class="email">
  <header class="masthead">
    <div class="brand"><span class="brand-dot"></span><span class="brand-name">CampusLedger.org</span></div>
  </header>

  <section class="hero-band">
    <h1 class="hero-title">Sample Title</h1>
    <p class="hero-subtitle">subtitle text here and more</p>
  </section>

  <div class="hero-photo" role="img" aria-label="Photo of a group of college students chatting and laughing outdoors on a sunny campus"></div>

  <a class="cta">
    <div class="cta-title">CALL TO ACTION</div>
    <div class="cta-text">subtext to the CTA, find out more...</div>
  </a>

  <section class="occupations">
    <div class="occupations-head">
      <span>Occupation Type</span><span>Median Salary</span><span>Next steps</span>
    </div>
    <div class="occupations-panel">
      <div class="occupation-row"><span>Ocupation sample 1<br>extra info</span><span>$90,300 per year*</span><span>Elementary and Secondary<br>School Programs</span></div>
      <div class="occupation-row"><span>Ocupation sample 2<br>extra info</span><span>$50,700 per year*</span><span>Educational, Guidance,<br>School</span></div>
      <div class="occupation-row"><span>Ocupation sample 3<br>extra info</span><span>$70,200 per year*</span><span>Elementary School Teachers,<br>Except Special Education</span></div>
      <div class="occupation-row"><span>Ocupation sample 4<br>other info</span><span>$55,900 per year*</span><span>Elementary and Secondary<br>School Programs</span></div>
      <div class="occupation-row"><span>Ocupation sample 5<br>otther exrta info</span><span>$60,200 per year*</span><span>Educational, Guidance,<br>School</span></div>
    </div>
  </section>

  <div class="footer-rule"></div>
  <footer class="footer">
    <div class="brand"><span class="brand-dot"></span><span class="brand-name">CampusLedger.org</span></div>
    <div class="footer-links">footer | contacts | other info</div>
  </footer>
</div>
</body>
</html>
```